Ridgewell Stonecraft Construction Needs business card

Hey we are in need of business card designs. I have upload our logo as a guideline, but free feel to run with it or come up with something unique.
Pls have fun with it and be creative. the name says it all!
i will give some directions after i see a few entries..
Logo source file has been uploaded..
Hey because of the logo is so colourful already.
Can we have a few submissions with less colour.
Also we are looking for clever/hidden/descriptive business card.

```html
<!DOCTYPE html>
<html lang="en">
<head>
<meta charset="utf-8">
<title>Ridgewell Stonecraft Construction – Business Card</title>
<link rel="stylesheet" href="https://fonts.googleapis.com/css2?family=Questrial&family=Montserrat:wght@700&display=swap">
<style>
  :root {
    --backdrop: #e4e2de;
    --card: #f4f4f3;
    --ink: #3c3c3e;
    --ink-soft: #5a5a5c;
    --accent-red: #e0202a;
    --tile-blue: #0a7cc1;
    --tile-yellow: #f2c012;
    --tile-green: #0c8a3e;
    --tile-charcoal: #3a3a3c;
  }
  * { box-sizing: border-box; margin: 0; padding: 0; }
  html, body { width: 1200px; height: 900px; overflow: hidden; }
  body {
    background: var(--backdrop);
    font-family: "Questrial", "Century Gothic", sans-serif;
    color: var(--ink);
    display: flex;
    flex-direction: column;
    align-items: center;
    justify-content: center;
    gap: 56px;
  }
  .card {
    width: 560px;
    height: 342px;
    background: var(--card);
    position: relative;
    overflow: hidden;
    box-shadow: 0 2px 10px rgba(0,0,0,0.12);
  }

  /* Front: company name */
  .card--front {
    display: flex;
    align-items: center;
    justify-content: center;
  }
  .brand {
    display: flex;
    align-items: center;
    gap: 14px;
    color: var(--ink-soft);
  }
  .brand__square {
    width: 30px;
    height: 30px;
    background: var(--ink-soft);
  }
  .brand__name {
    font-size: 27px;
    letter-spacing: 1px;
    text-transform: uppercase;
    line-height: 1.1;
  }
  .brand__sub {
    display: block;
    font-size: 11px;
    letter-spacing: 4px;
    margin-top: 4px;
  }

  /* Back: contact details */
  .contact {
    position: absolute;
    left: 42px;
    top: 44px;
  }
  .contact__name {
    font-family: "Montserrat", "Arial", sans-serif;
    font-weight: 700;
    font-size: 11px;
    letter-spacing: 2px;
    text-transform: uppercase;
  }
  .contact__role {
    font-size: 9px;
    letter-spacing: 2px;
    color: var(--accent-red);
    text-transform: uppercase;
    margin-top: 3px;
  }
  .contact__address {
    font-size: 10px;
    letter-spacing: 1.6px;
    text-transform: uppercase;
    line-height: 1.6;
    margin-top: 22px;
  }
  .contact__list {
    list-style: none;
    margin-top: 16px;
    font-size: 11px;
    letter-spacing: 1.5px;
  }
  .contact__item {
    display: flex;
    align-items: center;
    gap: 10px;
    height: 19px;
  }
  .contact__icon { width: 11px; height: 11px; flex: none; }

  .mosaic {
    position: absolute;
    inset: 0;
    background: linear-gradient(135deg, var(--tile-green) 0%, var(--tile-yellow) 30%, var(--accent-red) 52%, var(--tile-blue) 78%, var(--tile-charcoal) 100%);
    opacity: 0.85;
    clip-path: polygon(62% 38%, 100% 30%, 100% 100%, 0% 100%, 0% 84%, 40% 68%);
  }
</style>
</head>
<body>

  <section class="card card--front" aria-label="Card front">
    <div class="brand">
      <span class="brand__square"></span>
      <p class="brand__name">Ridgewell Stonecraft<span class="brand__sub">Construction</span></p>
    </div>
  </section>

  <section class="card card--back" aria-label="Card back">
    <div class="contact">
      <p class="contact__name">Marta Keane</p>
      <p class="contact__role">Director</p>
      <p class="contact__address">Unit 3, 212-216 Harbour Road<br>Kelvin Grove</p>
      <ul class="contact__list">
        <li class="contact__item">
          <svg class="contact__icon" viewBox="0 0 12 12"><circle cx="6" cy="6" r="6" fill="#e0202a"/><path d="M4 3.2 L5.2 3.2 L5.6 4.8 L4.9 5.4 Q5.6 6.8 6.8 7.2 L7.4 6.5 L8.9 7 L8.9 8.2 Q5 8.6 3.8 4.4 Z" fill="#fff"/></svg>
          <span>9381 2275</span>
        </li>
        <li class="contact__item">
          <svg class="contact__icon" viewBox="0 0 12 12"><circle cx="6" cy="6" r="6" fill="#e0202a"/><rect x="3.2" y="5" width="5.6" height="3.4" fill="#fff"/><rect x="4.2" y="3" width="3.6" height="2" fill="#fff"/></svg>
          <span>9381 2290</span>
        </li>
        <li class="contact__item">
          <svg class="contact__icon" viewBox="0 0 12 12"><circle cx="6" cy="6" r="6" fill="#e0202a"/><rect x="3" y="4" width="6" height="4" fill="#fff"/><path d="M3 4 L6 6.3 L9 4" stroke="#e0202a" stroke-width="0.8" fill="none"/></svg>
          <span>marta@ridgewellstone.com</span>
        </li>
        <li class="contact__item">
          <svg class="contact__icon" viewBox="0 0 12 12"><circle cx="6" cy="6" r="6" fill="#e0202a"/><circle cx="6" cy="6" r="3" fill="none" stroke="#fff" stroke-width="0.8"/><path d="M3 6 H9 M6 3 V9" stroke="#fff" stroke-width="0.8"/></svg>
          <span>www.ridgewellstone.com</span>
        </li>
      </ul>
    </div>
    <div class="mosaic" role="img" aria-label="Mosaic of coloured square tiles in blue, red, yellow, green and charcoal rising toward the corner"></div>
  </section>

</body>
</html>
```